Borealis Film and Design
Your Moments on Reels
Borealis Film and Design -
Creative Brief
Professional
Peter Vandrell
2187 Kettering Ln. North Pole, Alaska 99612
Peter@borealisfilmanddesign.example
borealisfilmanddesign.example

```html
<!DOCTYPE html>
<html lang="en">
<head>
<meta charset="utf-8">
<title>Borealis Film and Design – Business Card</title>
<link rel="stylesheet" href="https://fonts.googleapis.com/css2?family=Roboto:wght@400;500;700&display=swap">
<style>
  :root {
    --backdrop: #e9e7e3;
    --card: #ffffff;
    --navy: #1f2a5c;
    --royal: #2f3fae;
    --ink: #1d1d22;
    --band-dark: #0c0c0f;
    --divider: #6b6b6b;
    --white: #ffffff;
  }
  * { margin: 0; padding: 0; box-sizing: border-box; }
  html, body {
    width: 1200px; height: 804px; overflow: hidden;
    background: var(--backdrop);
    font-family: "Roboto", Arial, sans-serif;
  }
  .canvas { position: relative; width: 1200px; height: 804px; }
  .business-card {
    position: absolute; left: 100px; top: 161px;
    width: 1000px; height: 482px;
    background: var(--card);
    border-radius: 30px;
    overflow: hidden;
  }
  .brand {
    position: absolute; left: 0; right: 0; top: 58px;
    display: flex; justify-content: center; align-items: center; gap: 18px;
  }
  .brand-dot {
    width: 46px; height: 46px; border-radius: 50%;
    background: var(--royal);
  }
  .brand-name {
    font-size: 46px; font-weight: 700; color: var(--navy);
    letter-spacing: 1px; text-transform: uppercase;
  }
  .holder-name {
    position: absolute; left: 89px; top: 280px;
    font-size: 30px; font-weight: 500; color: var(--royal);
    letter-spacing: 1px; text-transform: uppercase;
  }
  .divider {
    position: absolute; left: 482px; top: 205px;
    width: 2px; height: 215px; background: var(--divider);
  }
  .contact {
    position: absolute; left: 518px; top: 244px;
    font-size: 23px; color: var(--ink); line-height: 40px;
    list-style: none;
  }
  .contact li { display: flex; align-items: center; gap: 10px; }
  .contact svg { width: 18px; height: 18px; fill: var(--navy); }
  .footer-bands { position: absolute; left: 0; bottom: 0; width: 1000px; height: 70px; }
  .web-address {
    position: absolute; right: 40px; bottom: 18px;
    font-size: 22px; color: var(--white);
  }
</style>
</head>
<body>
<main class="canvas">
  <section class="business-card">
    <div class="brand">
      <span class="brand-dot"></span>
      <span class="brand-name">Borealis Film and Design</span>
    </div>

    <p class="holder-name">Peter Vandrell</p>

    <span class="divider"></span>

    <ul class="contact">
      <li>2187 Kettering Ln.</li>
      <li>North Pole, Alaska 99612</li>
      <li>
        <svg viewBox="0 0 18 18" aria-hidden="true"><rect x="4" y="1" width="10" height="16" rx="2"/><rect x="6" y="3" width="6" height="9" fill="#fff"/></svg>
        1-907-555-0142
      </li>
      <li>
        <svg viewBox="0 0 18 18" aria-hidden="true"><rect x="1" y="3" width="16" height="12" rx="1"/><path d="M2 4 L9 10 L16 4" stroke="#fff" stroke-width="1.6" fill="none"/></svg>
        Peter@borealisfilmanddesign.example
      </li>
    </ul>

    <svg class="footer-bands" viewBox="0 0 1000 70" aria-hidden="true">
      <defs>
        <linearGradient id="blueBand" x1="0" x2="1" y1="0" y2="0">
          <stop offset="0" stop-color="#1d2a9c"/>
          <stop offset="0.7" stop-color="#3b4fd0"/>
          <stop offset="1" stop-color="#ffffff" stop-opacity="0.2"/>
        </linearGradient>
      </defs>
      <path d="M0 0 C 250 8, 450 14, 560 0 L 540 70 L 0 70 Z" fill="url(#blueBand)"/>
      <path d="M560 0 L 1000 0 L 1000 70 L 520 70 Z" fill="var(--band-dark)"/>
    </svg>
    <p class="web-address">www.borealisfilmanddesign.example</p>
  </section>
</main>
</body>
</html>
```